Fresh Tarrow Work Post - Business Card Required

Dear All,

I own Velmira Limited, which in turn owns the website:
www.harbinworkpost.example

I want all of you wonderful creative people to come up with a slick, and awesome business card design that incorporates the logo on the site, and some colouring and design elements from it.

You have free reign in how you go about doing this, I won't be giving my contact details on this platform, but the winner will be asked to redesign based on my contact details which I will supply at the end.

I need the design to be completed within 5 days. I need the final print copies of the business cards by the 25th November, so unfortunately it's a bit of a rush to get these designs ready.

Any questions, please ask.

Thank you
Updates

Thank you all for your hard work and exceptional designs provided. I do have to pick one, so I have a very clear idea of which one this is, however I will wait one further day until the competition closes to be fair to all those have submitted, or are in the process of submitting. I wish you all the best and thank you again for your dedication.

```html
<!DOCTYPE html>
<html lang="en">
<head>
<meta charset="utf-8">
<title>Harbin Work Post – Business Card</title>
<link rel="stylesheet" href="https://fonts.googleapis.com/css2?family=Cinzel:wght@400&family=Roboto:wght@400;700&display=swap">
<style>
  :root {
    --stage: #7a6c4c;
    --black: #141414;
    --band-grey: #3b3b3b;
    --silver: #cfd0d0;
    --white: #ffffff;
    --gold-dark: #a4782f;
    --gold: #d6b46a;
    --gold-light: #f4e7a5;
    --text-light: #e8e8e8;
    --rule: #8a8a8a;
  }
  * { margin: 0; padding: 0; box-sizing: border-box; }
  html, body { width: 1200px; height: 797px; overflow: hidden; }
  body { background: var(--stage); position: relative; font-family: "Roboto", Arial, sans-serif; }

  .card { position: absolute; overflow: hidden; border-radius: 22px; }

  /* Front (portrait) */
  .card-front { left: 185px; top: 110px; width: 285px; height: 502px; }
  .card-front svg { position: absolute; inset: 0; }
  .brand-mark {
    position: absolute; left: 0; width: 100%; top: 268px;
    text-align: center; font-family: "Cinzel", Georgia, serif; font-weight: 400;
    font-size: 26px; line-height: 34px; letter-spacing: 2px; color: var(--gold-dark);
  }
  .brand-footer {
    position: absolute; left: 44px; right: 37px; top: 432px; height: 31px;
    border-top: 2px solid var(--gold); border-bottom: 2px solid var(--gold);
    display: flex; align-items: center; justify-content: center;
    font-family: "Cinzel", Georgia, serif; font-size: 17px; letter-spacing: 2px; color: var(--gold);
    white-space: nowrap;
  }

  /* Back (landscape) */
  .card-back {
    left: 572px; top: 285px; width: 503px; height: 287px;
    background: radial-gradient(ellipse at 45% 45%, #2e2e2e 0%, var(--black) 75%);
  }
  .holder {
    position: absolute; right: 275px; top: 113px;
    text-align: right; white-space: nowrap;
  }
  .holder-name {
    font-family: "Cinzel", Georgia, serif; font-size: 24px; letter-spacing: 0.5px;
    color: var(--text-light); line-height: 30px;
  }
  .holder-role { font-weight: 700; font-size: 16px; color: var(--white); margin-top: 8px; }
  .divider { position: absolute; left: 238px; top: 114px; width: 1px; height: 62px; background: var(--rule); }
  .contact-list {
    position: absolute; left: 248px; top: 117px; list-style: none;
    font-size: 11.5px; color: var(--text-light); line-height: 14.5px; white-space: nowrap;
  }
  .contact-list li { display: flex; align-items: flex-start; }
  .contact-list svg { width: 10px; height: 10px; margin: 2px 14px 0 0; flex: none; fill: var(--text-light); }
  .contact-list .spacer { width: 10px; margin-right: 14px; flex: none; }
  .web-band {
    position: absolute; left: 0; right: 0; top: 235px; height: 28px; background: var(--band-grey);
    display: flex; align-items: center; justify-content: center; font-size: 11px; color: var(--text-light);
  }
  .gold-band {
    position: absolute; left: 0; right: 0; top: 263px; height: 24px;
    background: linear-gradient(90deg, var(--gold-dark), var(--gold) 30%, var(--gold-light) 55%, var(--gold) 75%, var(--gold-dark));
  }
</style>
</head>
<body>

<section class="card card-front" aria-label="Business card front">
  <svg viewBox="0 0 285 502" width="285" height="502" aria-hidden="true">
    <defs>
      <linearGradient id="top-black" x1="0" y1="0" x2="1" y2="0">
        <stop offset="0" stop-color="#1a1a1a"/><stop offset="0.6" stop-color="#3c3c3c"/><stop offset="1" stop-color="#6a6a6a"/>
      </linearGradient>
      <linearGradient id="gold-sweep" x1="0" y1="0" x2="1" y2="0">
        <stop offset="0" stop-color="#a4782f"/><stop offset="0.35" stop-color="#d6b46a"/>
        <stop offset="0.7" stop-color="#f4e7a5"/><stop offset="1" stop-color="#b88d3e"/>
      </linearGradient>
      <linearGradient id="base-black" x1="0" y1="0" x2="0" y2="1">
        <stop offset="0" stop-color="#2b2b2b"/><stop offset="0.5" stop-color="#111"/><stop offset="1" stop-color="#262626"/>
      </linearGradient>
    </defs>
    <rect width="285" height="502" fill="url(#top-black)"/>
    <path d="M0,22 Q70,30 90,160 L0,175 Z" fill="var(--silver)"/>
    <path d="M285,22 Q220,30 205,150 L285,160 Z" fill="var(--silver)"/>
    <path d="M0,178 Q142,95 285,160 V502 H0 Z" fill="var(--white)"/>
    <path d="M0,195 Q142,118 285,178 V502 H0 Z" fill="url(#gold-sweep)"/>
    <path d="M0,335 Q50,210 160,212 Q250,216 285,290 V405 H0 Z" fill="var(--white)"/>
    <rect y="405" width="285" height="97" fill="url(#base-black)"/>
  </svg>
  <div class="brand-mark">Harbin<br>Work Post</div>
  <div class="brand-footer">HARBIN WORK POST</div>
</section>

<section class="card card-back" aria-label="Business card back">
  <div class="holder">
    <p class="holder-name">CORVIN HALE</p>
    <p class="holder-role">Managing Director</p>
  </div>
  <div class="divider"></div>
  <ul class="contact-list">
    <li><svg viewBox="0 0 10 10" aria-hidden="true"><path d="M2,0 L4,2.5 L3,3.6 Q4.2,6 6.4,7 L7.5,6 L10,8 L8.5,10 Q1,8 0,1.5 Z"/></svg>0700 900 4123</li>
    <li><svg viewBox="0 0 10 10" aria-hidden="true"><path d="M5,0.5 L10,5 H8.5 V9.5 H6 V6.5 H4 V9.5 H1.5 V5 H0 Z"/></svg>12 Elmstead Row, Harbin,</li>
    <li><span class="spacer"></span>Tarrow, W9 4QX</li>
    <li><svg viewBox="0 0 10 10" aria-hidden="true"><path d="M0,2 H10 V8.5 H0 Z M0.8,2.6 L5,5.6 L9.2,2.6" stroke="#141414" stroke-width="0.8"/></svg>contact@harbinworkpost.example</li>
  </ul>
  <div class="web-band">www.harbinworkpost.example</div>
  <div class="gold-band"></div>
</section>

</body>
</html>
```